New UI for electricity data tool

We are looking for a new UI for the website http://vantorgrid.net. Reassessing the structure of the website is as important as specific design choices. We have created a uniquely comprehensive set of global electricity generation data and now we are looking for creative solutions for how to make this data accessible. Researching and referencing other similar projects may be a good idea.

Goals:
• The website should clearly communicate the most important general conclusions that can be drawn from the data, including:
◦ The world as a whole is not moving away from fossil fuels for electricity generation
◦ There are substantial differences between regions
▪ Some regions have basically solved the problem – they already generate almost all of their electricity from non-fossil sources
▪ Some regions have greatly improved in terms of decarbonizing their electricity generation.
▪ Some regions have greatly deteriorated, in other words they are using a much higher share of fossil fuels to generate their electricity.
◦ There are substantial differences between energy sources. Regions that have successfully decarbonized their electricity generation have usually done so using hydro and/or nuclear. Other low-carbon energy sources have grown quickly in relative terms in the last few years but are so far contributing little in absolute numbers.
• The website should serve as inspiration for energy policy debates. The goal is to study the impact of existing policies around the world. Energy policy here refers to particular combinations of energy sources – ie how much have the countries invested in each type of electricity generation. The tool should help answer questions such as:
◦ Which countries have done the most in terms of decarbonizing their electricity generation?
◦ Which types of energy polices have lead to the fastest decarbonization processes around the world?
◦ If country A changed its energy policy to be more like country B, what would the likely impact be?

Challenges:
• There is a lot of data – it can be overwhelming to the user. It’s crucial to make the site easy to navigate. The main page should highlight the most important data, and it should also be straightforward to find more detailed data.
• Data availability varies from region to region. The current interface addresses this with the default option “Exclude regions with limited data”. We expect a better approach to dealing with this issue. For some regions and years energy sources are grouped together as for example “other renewables” whereas in other cases more detailed data is available.
• Credibility is crucial. Our data is based on a combination of data from KQ and the Tessary Trust. It must be very clear throughout the site where each data set comes from.

Details:
• The current chart color schemes is loosely based on the carbon emissions from each energy source. This should not necessarily be so. The goal is to on the one hand communicate clearly the amounts of fossil vs non-fossil energy that are generated by each region. At the same time we also want to make it easy to view specific energy sources.

Inspirational websites:
• https://www.grafmelo.org/
• https://trendquarrily.org/

Let's simplify. The main metric to focus on is Brisavolt Index and the extent to which the world and each country has achieved it (eg Iceland 100%, France 88% and so on). I'm considering changing the name of the site to BrisavoltIndex.org. We can use maps, charts and perhaps other tools to communicate this main message. What's the best way of doing this?

```html
<!DOCTYPE html>
<html lang="en">
<head>
<meta charset="utf-8">
<title>VantorGrid.net — Clean Electricity</title>
<link href="https://fonts.googleapis.com/css2?family=Jost:wght@300;400;500;700&display=swap" rel="stylesheet">
<style>
  :root {
    --bg-violet: #5447d4;
    --globe-light: #3e2fe0;
    --globe-mid: #3322b8;
    --globe-dark: #1e1262;
    --text-white: #ffffff;
    --button-ink: #5447d4;
  }
  * { margin: 0; padding: 0; box-sizing: border-box; }
  html, body {
    width: 1200px;
    height: 675px;
    overflow: hidden;
  }
  body {
    background: var(--bg-violet);
    color: var(--text-white);
    font-family: "Jost", "Helvetica Neue", Arial, sans-serif;
    position: relative;
  }
  .globe-visual {
    position: absolute;
    top: 0;
    left: 0;
    width: 1200px;
    height: 675px;
  }
  .site-header {
    position: absolute;
    top: 30px;
    left: 50px;
    right: 50px;
    display: flex;
    justify-content: space-between;
    align-items: center;
  }
  .site-wordmark {
    font-size: 15px;
    font-weight: 500;
    letter-spacing: 0.2px;
    color: var(--text-white);
    text-decoration: none;
  }
  .menu-toggle {
    width: 16px;
    height: 14px;
    display: block;
  }
  .hero {
    position: absolute;
    left: 142px;
    top: 236px;
  }
  .hero-title {
    font-size: 68px;
    line-height: 68px;
    letter-spacing: 0.5px;
  }
  .hero-title .title-strong {
    display: block;
    font-weight: 700;
  }
  .hero-title .title-light {
    display: block;
    font-weight: 300;
    letter-spacing: 2px;
  }
  .hero-lede {
    margin-top: 30px;
    width: 290px;
    font-size: 12.5px;
    line-height: 17.5px;
    font-weight: 400;
  }
  .explore-button {
    margin-top: 44px;
    display: inline-flex;
    align-items: center;
    height: 33px;
    padding: 0 14px 0 3px;
    background: var(--text-white);
    border-radius: 17px;
    color: var(--button-ink);
    font-size: 10px;
    font-weight: 500;
    letter-spacing: 0.8px;
    text-decoration: none;
  }
  .explore-button .arrow-disc {
    width: 27px;
    height: 27px;
    border-radius: 50%;
    background: var(--button-ink);
    display: flex;
    align-items: center;
    justify-content: center;
    margin-right: 10px;
  }
  .data-partners {
    position: absolute;
    left: 142px;
    top: 622px;
    display: flex;
    align-items: center;
    gap: 22px;
    font-size: 11px;
    font-weight: 500;
    letter-spacing: 0.3px;
  }
  .partner {
    display: flex;
    align-items: center;
    gap: 6px;
  }
  .partner-dot {
    width: 18px;
    height: 18px;
    border-radius: 50%;
    background: var(--text-white);
    opacity: 0.85;
  }
</style>
</head>
<body>
  <svg class="globe-visual" viewBox="0 0 1200 675" role="img" aria-label="Dotted globe illustration of world electricity data">
    <defs>
      <radialGradient id="globeShade" cx="0.15" cy="0.5" r="0.95">
        <stop offset="0" stop-color="var(--globe-light)"/>
        <stop offset="0.55" stop-color="var(--globe-mid)"/>
        <stop offset="1" stop-color="var(--globe-dark)"/>
      </radialGradient>
    </defs>
    <ellipse cx="1075" cy="337" rx="390" ry="395" fill="url(#globeShade)"/>
  </svg>

  <header class="site-header">
    <a class="site-wordmark" href="#">VantorGrid.net</a>
    <svg class="menu-toggle" viewBox="0 0 16 14" aria-label="Menu">
      <rect x="5" y="0" width="8" height="1.6" fill="#fff"/>
      <rect x="0" y="6" width="16" height="1.6" fill="#fff"/>
      <rect x="3" y="12" width="10" height="1.6" fill="#fff"/>
    </svg>
  </header>

  <main class="hero">
    <h1 class="hero-title">
      <span class="title-strong">Clean</span>
      <span class="title-light">Electricity</span>
    </h1>
    <p class="hero-lede">A uniquely comprehensive set of global electricity generation data</p>
    <a class="explore-button" href="#">
      <span class="arrow-disc">
        <svg width="12" height="12" viewBox="0 0 12 12">
          <path d="M1 6h10M6.5 1.5 11 6l-4.5 4.5" fill="none" stroke="#fff" stroke-width="1.4" stroke-linecap="round" stroke-linejoin="round"/>
        </svg>
      </span>
      EXPLORE THE DATA
    </a>
  </main>

  <footer class="data-partners">
    <span class="partner"><span class="partner-dot"></span>KQ</span>
    <span class="partner"><span class="partner-dot"></span>Tessary Trust</span>
  </footer>
</body>
</html>
```